Fennick Executive Search - New Business Card Design Project

We are an executive search firm called Fennick Executive Search based in the UK. We require a custom design for a business card. We're looking to convey a professional service to executives for executive search recruitment services. In terms of colours, we like dark blues and grays (maybe even silver incorporated somewhere if we go for a foiled type of card) but we're open to your artistic flare. See our current logo in attachments. We are totally open on design so long as the design is slick and professional.
Updates

Thanks for all your contributions of various designs. I have to say the quality of work has been amazing which is going to make our job quite difficult in the coming days on making a decision. Thanks to you all that have taken the time to submit designs thus far. We'll keep on reviewing and try to narrow down our selection as soon as possible.

Target Market(s)

Executive Search

Industry/Entity Type

Recruitment

Contact Information for Business Card

Fennick Executive Search,
Exclusively Sourcing & Hiring Senior Leaders
Gordon Pellbury, Managing Director,
07823 906417
0117 486 7132
gordon@fennickexecutive.co.uk
fennickexecutive.co.uk
58 Lindmoor Court, Hatherley Road, Bristol, BS32 9QJ

Font styles to use
Sans Serif
Other font styles liked:
• Roboto (which is used in our logo)

Requirements
Must have
• Our logo (It has a subtle fade on it from #02071d at top to #333649 at bottom)
• The logo can be on one side or both sides
• Must be elegant and professional
• We have 2nd slogan CONSULT | INSPIRE | INNOVATE | DELIVER which can be incorporated into the card
Nice to have
• Use of blues and grey colours
• Compatible with similar styling to our website fennickexecutive.co.uk
Should not have
• Must not be overly brash
• Must not contain cartoon characters

```html
<!DOCTYPE html>
<html lang="en">
<head>
<meta charset="utf-8">
<title>Fennick Executive Search – Business Card</title>
<link rel="stylesheet" href="https://fonts.googleapis.com/css2?family=Roboto:wght@400;500;700&display=swap">
<style>
  :root {
    --backdrop: #2b2b2d;
    --navy-top: #02071d;
    --navy-mid: #1c2454;
    --navy-bottom: #333649;
    --silver: #e9eaec;
    --silver-dark: #cfd1d6;
    --ink: #1a1c2a;
    --ink-soft: #3a3d4d;
    --white: #ffffff;
    --rule: #1b2150;
  }
  * { box-sizing: border-box; margin: 0; padding: 0; }
  html, body {
    width: 1200px; height: 997px; overflow: hidden;
    background: var(--backdrop);
    font-family: "Roboto", Arial, sans-serif;
  }
  .canvas { position: relative; width: 1200px; height: 997px; }

  .card {
    position: absolute;
    width: 560px; height: 320px;
    border-radius: 4px;
    overflow: hidden;
    box-shadow: 0 18px 40px rgba(0,0,0,.45);
  }

  /* Reverse side */
  .card--reverse {
    left: 80px; top: 110px;
    background: linear-gradient(180deg, var(--navy-mid) 0%, var(--navy-top) 100%);
    color: var(--white);
    display: flex; flex-direction: column; align-items: center; justify-content: space-between;
    padding: 38px 30px 34px;
  }
  .slogan {
    font-size: 14px; letter-spacing: 3px; font-weight: 400;
    color: var(--silver-dark);
  }
  .wordmark {
    font-weight: 500; color: var(--white);
    letter-spacing: 2px; text-transform: uppercase;
    display: flex; align-items: center; gap: 12px;
  }
  .wordmark__mark {
    width: 14px; height: 14px; background: var(--white); display: inline-block;
  }
  .card--reverse .wordmark { font-size: 26px; }
  .website {
    font-size: 15px; letter-spacing: 3px; text-transform: uppercase; color: var(--silver);
  }

  /* Front side */
  .card--front {
    left: 560px; top: 520px;
    background: linear-gradient(180deg, var(--navy-mid) 0%, var(--navy-top) 100%);
  }
  .front__head {
    position: absolute; left: 0; right: 0; top: 0; height: 150px;
    display: flex; align-items: center; justify-content: center;
  }
  .card--front .wordmark { font-size: 24px; }
  .front__band {
    position: absolute; left: 0; right: 0; top: 168px; height: 100px;
    background: linear-gradient(180deg, var(--white) 0%, var(--silver) 100%);
    display: flex; align-items: center;
    border-top: 3px solid var(--silver);
    border-bottom: 3px solid var(--silver);
    outline: 2px solid var(--rule);
    outline-offset: -5px;
  }
  .person { flex: 1; padding-left: 54px; }
  .person__name { font-size: 17px; font-weight: 700; color: var(--ink); letter-spacing: .5px; text-transform: uppercase; }
  .person__role { font-size: 14px; font-weight: 700; color: var(--ink-soft); margin-top: 2px; padding-left: 26px; }
  .band__divider { width: 2px; height: 64px; background: linear-gradient(180deg, transparent, var(--rule), transparent); }
  .contacts { flex: 1.3; list-style: none; padding-left: 26px; }
  .contacts li { display: flex; align-items: center; gap: 10px; font-size: 13.5px; color: var(--ink-soft); line-height: 22px; }
  .contacts svg { width: 14px; height: 14px; flex: none; }
  .front__address {
    position: absolute; left: 0; right: 0; bottom: 0; height: 46px;
    display: flex; align-items: center; justify-content: center;
    font-size: 14px; color: var(--silver-dark); letter-spacing: .5px;
  }
</style>
</head>
<body>
<main class="canvas">
  <section class="card card--reverse" aria-label="Business card, reverse side">
    <p class="slogan">CONSULT | INSPIRE | INNOVATE | DELIVER</p>
    <p class="wordmark"><span class="wordmark__mark"></span>Fennick Executive Search</p>
    <p class="website">www.fennickexecutive.co.uk</p>
  </section>

  <section class="card card--front" aria-label="Business card, front side">
    <div class="front__head">
      <p class="wordmark"><span class="wordmark__mark"></span>Fennick Executive Search</p>
    </div>
    <div class="front__band">
      <div class="person">
        <p class="person__name">Gordon Pellbury</p>
        <p class="person__role">Managing Director</p>
      </div>
      <span class="band__divider"></span>
      <ul class="contacts">
        <li>
          <svg viewBox="0 0 14 14" aria-hidden="true"><circle cx="7" cy="7" r="7" fill="#1a1c2a"/><path d="M3.5 6.2c0-1.4 7-1.4 7 0v.8H9V6.2H5V7H3.5z M4.5 8h5v2h-5z" fill="#fff"/></svg>
          07823 906417
        </li>
        <li>
          <svg viewBox="0 0 14 14" aria-hidden="true"><circle cx="7" cy="7" r="7" fill="#1a1c2a"/><rect x="5" y="3.5" width="4" height="2.5" fill="#fff"/><rect x="3.5" y="6" width="7" height="3" rx=".5" fill="#fff"/><rect x="5" y="8.5" width="4" height="2" fill="#fff"/></svg>
          0117 486 7132
        </li>
        <li>
          <svg viewBox="0 0 14 14" aria-hidden="true"><circle cx="7" cy="7" r="7" fill="#1a1c2a"/><rect x="3.5" y="4.5" width="7" height="5" fill="#fff"/><path d="M3.5 4.5 7 7.5l3.5-3" fill="none" stroke="#1a1c2a" stroke-width=".8"/></svg>
          gordon@fennickexecutive.co.uk
        </li>
      </ul>
    </div>
    <p class="front__address">58 Lindmoor Court, Hatherley Road, Bristol, BS32 9QJ</p>
  </section>
</main>
</body>
</html>
```